The Lantern Guide

I am a life coach specializing in helping people with depression and bipolar disorder. I would like a nice, fun design for a business card.

```html
<!DOCTYPE html>
<html lang="en">
<head>
<meta charset="utf-8">
<title>The Lantern Guide – Business Card</title>
<link rel="stylesheet" href="https://fonts.googleapis.com/css2?family=Libre+Baskerville:wght@700&display=swap">
<style>
  :root {
    --page-bg: #ecebe8;
    --card-white: #ffffff;
    --silver-light: #ececec;
    --silver-mid: #c4c4c6;
    --silver-dark: #8d8d90;
    --indigo-light: #b7b9dc;
    --indigo-mid: #7a7fb4;
    --indigo-dark: #3f4787;
    --ink: #2b2b2d;
  }
  * { margin: 0; padding: 0; box-sizing: border-box; }
  html, body {
    width: 1200px;
    height: 1200px;
    overflow: hidden;
    background: var(--page-bg);
  }
  .canvas {
    position: relative;
    width: 1200px;
    height: 1200px;
  }
  .business-card {
    position: absolute;
    left: 75px;
    top: 285px;
    width: 1050px;
    height: 630px;
    background: var(--card-white);
    box-shadow: 0 14px 36px rgba(0, 0, 0, 0.18);
    overflow: hidden;
  }
  .card-shapes {
    position: absolute;
    inset: 0;
    width: 100%;
    height: 100%;
    display: block;
  }
  .brand {
    position: absolute;
    left: 70px;
    top: 190px;
    display: flex;
    align-items: center;
    gap: 18px;
  }
  .brand-mark {
    width: 22px;
    height: 22px;
    background: var(--ink);
  }
  .brand-name {
    font-family: "Libre Baskerville", "Times New Roman", serif;
    font-weight: 700;
    font-size: 46px;
    letter-spacing: 1px;
    text-transform: uppercase;
    color: var(--ink);
    line-height: 1;
  }
  .brand-rule {
    position: absolute;
    left: 110px;
    top: 258px;
    width: 560px;
    height: 3px;
    background: var(--ink);
  }
</style>
</head>
<body>
  <div class="canvas">
    <div class="business-card">
      <svg class="card-shapes" viewBox="0 0 1000 600" preserveAspectRatio="none" aria-hidden="true">
        <defs>
          <linearGradient id="silverFill" x1="0" y1="0" x2="1" y2="1">
            <stop offset="0" stop-color="var(--silver-dark)"/>
            <stop offset="0.45" stop-color="var(--silver-mid)"/>
            <stop offset="1" stop-color="var(--silver-light)"/>
          </linearGradient>
          <radialGradient id="indigoFill" cx="0.62" cy="0.28" r="0.8">
            <stop offset="0" stop-color="var(--indigo-light)"/>
            <stop offset="0.45" stop-color="var(--indigo-mid)"/>
            <stop offset="1" stop-color="var(--indigo-dark)"/>
          </radialGradient>
        </defs>
        <path class="silver-sweep" fill="url(#silverFill)"
              d="M0,0 H795 C775,260 645,470 435,558 C392,576 345,585 295,585 H95 C50,585 22,556 22,512 V110 C22,66 12,34 0,20 Z"/>
        <path class="indigo-sweep" fill="url(#indigoFill)"
              d="M470,600 C625,520 705,365 765,225 C802,142 862,112 922,112 C966,112 988,142 988,192 V540 C988,575 965,600 930,600 Z"/>
      </svg>
      <div class="brand">
        <span class="brand-mark"></span>
        <span class="brand-name">The Lantern Guide</span>
      </div>
      <div class="brand-rule"></div>
    </div>
  </div>
</body>
</html>
```